Bramwell Pricing Parallel Gauge

I want a landing page for them to click on the logo with a brief description of the site.

Once they click on the logo, it will take them to make a decision for two types of insurance. One will be health and the other will be home/auto.

I will need an iframe for the home/auto and it will take them to a site (which is already built) for them to get a quote.

I will need a separate iframe for the health to take them to separate site (which is built) for them to get a quote.

Target Market(s)

18-45 Year olds who want to go online for insurance quotes. This is for quoting primarily and not an information site.

Industry/Entity Type

Health

Requirements
Must have
• Sleek and sexy. I have a logo as well.

May want the following on the landing page:
Georgia's FIRST Insurance Exchange for Home, Auto, and Health Insurance

No Hassle, Real-time, Quotes - As a Matter of fact... You call us if interested, We dont sell your information and Most Importantly… its free!!

Give it a shot… Click on the logo to get started and if you are interested in one of the many carriers we represent, call us.
Should not have
• Don't want the typical website. I want this to be different than all template boxes.

```html
<!DOCTYPE html>
<html lang="en">
<head>
<meta charset="utf-8">
<title>Bramwell Pricing Parallel Gauge – Landing Pages</title>
<link rel="stylesheet" href="https://fonts.googleapis.com/css2?family=Cinzel:wght@400;500&family=Questrial&family=Stardos+Stencil:wght@700&display=swap">
<style>
  :root {
    --ink: #111111;
    --brand-red: #d0202e;
    --brand-blue: #1a6fc0;
    --wordmark: #232323;
    --paper: #ffffff;
    --board: #ffffff;
    --shadow: rgba(0, 0, 0, 0.5);
  }
  * { margin: 0; padding: 0; box-sizing: border-box; }
  html, body {
    width: 720px; height: 1200px; overflow: hidden;
    background: var(--board);
  }
  .board {
    position: relative;
    width: 720px; height: 1200px;
    background: var(--board);
    color: var(--ink);
  }
  .page {
    position: absolute;
    background: var(--paper);
    box-shadow: 7px 7px 14px var(--shadow);
  }
  .page--intro  { left: 131px; top: 17px;  width: 456px; height: 542px; }
  .page--choice { left: 186px; top: 610px; width: 365px; height: 567px; }

  .headline {
    position: absolute; left: 0; right: 0;
    text-align: center;
    font-family: "Stardos Stencil", "Stencil", serif;
    font-weight: 700;
    text-transform: uppercase;
    font-size: 30px;
    letter-spacing: 0.5px;
    white-space: nowrap;
  }
  .headline .cap { font-size: 42px; }
  .page--intro .headline  { top: 40px; }
  .page--choice .headline { top: 6px; }
  .red  { color: var(--brand-red); }
  .blue { color: var(--brand-blue); }

  .brand {
    position: absolute; left: 0; right: 0;
    display: block;
    text-align: center;
    color: var(--wordmark);
    text-decoration: none;
  }
  .brand__dot {
    display: block;
    margin: 0 auto;
    width: 92px; height: 92px;
    border-radius: 50%;
    background: var(--brand-red);
  }
  .brand__name {
    display: block;
    font-family: "Questrial", "Helvetica Neue", sans-serif;
    font-weight: 400;
    color: var(--wordmark);
    line-height: 1;
    letter-spacing: 1px;
    white-space: nowrap;
  }
  .page--intro .brand  { top: 118px; }
  .page--intro .brand__name  { font-size: 36px; margin-top: 28px; }
  .page--choice .brand { top: 102px; }
  .page--choice .brand__name { font-size: 42px; margin-top: 41px; }

  .pitch {
    position: absolute; left: 102px; top: 289px;
    font-family: "Cinzel", "Copperplate", serif;
    font-weight: 500;
    font-size: 22px;
    line-height: 41px;
    letter-spacing: 0.5px;
    white-space: nowrap;
    list-style: none;
  }
  .pitch__lead { font-size: 27px; letter-spacing: 0; }
  .pitch__call {
    font-family: "Stardos Stencil", "Stencil", serif;
    font-weight: 700;
    text-transform: uppercase;
    font-size: 26px;
    margin-top: 2px;
  }
  .pitch__call .cap { font-size: 36px; }

  .quote-title {
    position: absolute; left: 0; right: 0; top: 330px;
    text-align: center;
    font-family: "Questrial", "Helvetica Neue", sans-serif;
    font-size: 44px;
    white-space: nowrap;
  }
  .quote-title .cap {
    font-family: "Stardos Stencil", "Stencil", serif;
    font-weight: 700;
    font-size: 56px;
  }
  .quote-option {
    position: absolute; left: 97px;
    font-family: "Questrial", "Helvetica Neue", sans-serif;
    font-size: 42px;
    white-space: nowrap;
    color: var(--ink);
    text-decoration: none;
  }
  .quote-option--home   { top: 429px; }
  .quote-option--health { top: 505px; }

  .caption {
    position: absolute;
    font-family: "Cinzel", "Copperplate", serif;
    font-weight: 500;
    font-size: 17px;
    white-space: nowrap;
  }
  .caption--intro  { left: 11px; top: 590px; }
  .caption--choice { left: 14px; top: 672px; }

  .arrows {
    position: absolute; left: 0; top: 0;
    width: 720px; height: 1200px;
    pointer-events: none;
  }
  .arrow { stroke: var(--ink); stroke-width: 3.5; fill: none; }
  .pointer { stroke: var(--ink); stroke-width: 2.5; fill: none; }
</style>
</head>
<body>
<main class="board">

  <section class="page page--intro" aria-label="Landing page 1">
    <h1 class="headline"><span class="cap red">G</span>ive it a <span class="cap blue">S</span>hot</h1>
    <a class="brand" href="#choose">
      <span class="brand__dot" aria-hidden="true"></span>
      <span class="brand__name">BPG QUOTES</span>
    </a>
    <ul class="pitch">
      <li class="pitch__lead">Click on the Logo</li>
      <li>to get started</li>
      <li>if you are interested</li>
      <li>in one of the many</li>
      <li>carriers we represent</li>
      <li class="pitch__call"><span class="cap red">C</span>all <span class="cap blue">U</span>s</li>
    </ul>
  </section>

  <section class="page page--choice" id="choose" aria-label="Landing page 2">
    <h2 class="headline"><span class="cap red">G</span>ive it a <span class="cap blue">S</span>hot</h2>
    <div class="brand">
      <span class="brand__dot" aria-hidden="true"></span>
      <span class="brand__name">BPG QUOTES</span>
    </div>
    <h3 class="quote-title"><span class="cap">G</span>et a <span class="cap">Q</span>uote</h3>
    <a class="quote-option quote-option--home" href="#home-car"><span class="red">H</span>ome&amp;<span class="blue">C</span>ar</a>
    <a class="quote-option quote-option--health" href="#health"><span class="red">H</span>ealth</a>
  </section>

  <p class="caption caption--intro">Landing page 1</p>
  <p class="caption caption--choice">Landing page 2</p>

  <svg class="arrows" viewBox="0 0 720 1200" aria-hidden="true">
    <defs>
      <marker id="head" viewBox="0 0 10 10" refX="8" refY="5" markerWidth="5" markerHeight="5" orient="auto-start-reverse" markerUnits="strokeWidth">
        <path d="M0 0 L10 5 L0 10 Z" fill="#111"/>
      </marker>
      <marker id="fletch" viewBox="0 0 12 10" refX="2" refY="5" markerWidth="6" markerHeight="5" orient="auto" markerUnits="strokeWidth">
        <path d="M0 0 L6 0 L12 5 L6 10 L0 10 L6 5 Z" fill="#111"/>
      </marker>
      <marker id="tip" viewBox="0 0 10 10" refX="9" refY="5" markerWidth="6" markerHeight="6" orient="auto" markerUnits="strokeWidth">
        <path d="M0 0 L10 5 L0 10 Z" fill="#111"/>
      </marker>
    </defs>

    <g class="arrow" marker-start="url(#fletch)" marker-end="url(#head)">
      <line x1="169" y1="103" x2="260" y2="154"/>
      <line x1="146" y1="185" x2="245" y2="185"/>
      <line x1="169" y1="277" x2="257" y2="228"/>
      <line x1="536" y1="82"  x2="448" y2="131"/>
      <line x1="576" y1="182" x2="477" y2="171"/>
      <line x1="553" y1="264" x2="462" y2="219"/>
      <line x1="200" y1="1061" x2="279" y2="1061"/>
      <line x1="519" y1="1141" x2="428" y2="1141"/>
    </g>

    <g class="pointer" marker-end="url(#tip)">
      <line x1="62" y1="587" x2="110" y2="553"/>
      <line x1="126" y1="707" x2="166" y2="756"/>
    </g>
  </svg>

</main>
</body>
</html>
```